Marrowind Lake Billboard

Looking to design a multi purpose billboard promoting Marrowind Lake as a destination point. Billboard size is 12ft x 40ft
My goal is to advertise our restaurant The Driftmill (pic attached)
What makes Marrowind a destination? It offers lodging / water skiing / Off Road Adventure / Camping / Fishing / Hunting
Want a catch phrase, something like "Looking For a Getaway" or "Need a Break"
Needs to really pop and catch the interest of the looker
maybe have our website address www.marrowinddriftmill.example
Open for ideas

```html
<!DOCTYPE html>
<html lang="en">
<head>
<meta charset="utf-8">
<title>Marrowind Lake Billboard</title>
<link rel="stylesheet" href="https://fonts.googleapis.com/css2?family=Mr+Dafoe&family=Oswald:wght@500;700&display=swap">
<style>
  :root {
    --stage: #e4e4e4;
    --sun-light: #ffc400;
    --sun-deep: #ffad00;
    --accent-red: #e8150f;
    --ink: #2b1d0e;
    --paper: #ffffff;
    --photo-light: #f7c21a;
    --photo-deep: #e0a800;
    --sketch: #e29c00;
  }
  html, body {
    margin: 0;
    padding: 0;
    width: 1200px;
    height: 962px;
    overflow: hidden;
    background: var(--stage);
  }
  .billboard {
    position: absolute;
    left: 20px;
    top: 333px;
    width: 1160px;
    height: 295px;
    display: block;
  }
  .headline {
    font-family: "Mr Dafoe", cursive;
    fill: var(--accent-red);
  }
  .brand-name {
    font-family: "Oswald", sans-serif;
    font-weight: 700;
    fill: var(--ink);
    letter-spacing: 2px;
  }
  .offers-title {
    font-family: "Oswald", sans-serif;
    font-weight: 700;
    fill: var(--paper);
  }
  .offers-list {
    font-family: "Oswald", sans-serif;
    font-weight: 500;
    fill: var(--paper);
  }
</style>
</head>
<body>
<svg class="billboard" viewBox="0 0 1860 473" preserveAspectRatio="none" xmlns="http://www.w3.org/2000/svg">
  <defs>
    <linearGradient id="sun-fill" x1="0" y1="0" x2="1" y2="1">
      <stop offset="0" stop-color="var(--sun-light)"/>
      <stop offset="1" stop-color="var(--sun-deep)"/>
    </linearGradient>
    <linearGradient id="photo-fill" x1="0" y1="0" x2="1" y2="1">
      <stop offset="0" stop-color="var(--photo-light)"/>
      <stop offset="1" stop-color="var(--photo-deep)"/>
    </linearGradient>
  </defs>

  <rect class="backdrop" x="0" y="0" width="1860" height="473" fill="url(#sun-fill)"/>

  <path class="wave-top" d="M1060 0 C1120 40 1200 62 1300 62 C1420 62 1530 30 1600 0 Z" fill="var(--paper)"/>
  <path class="wave-right" d="M1815 0 C1860 30 1845 100 1810 180 C1770 270 1750 380 1795 473 L1860 473 L1860 0 Z" fill="var(--paper)"/>
  <path class="wave-left" d="M0 262 C40 268 62 300 56 350 C50 400 30 440 22 473 L0 473 Z" fill="var(--paper)"/>

  <rect class="photo-angler" x="600" y="0" width="490" height="473" fill="url(#photo-fill)" role="img" aria-label="Photo of a smiling angler in a yellow raincoat and bucket hat holding a fishing rod with a caught fish and a landing net"/>

  <rect class="sketch-fish" x="1233" y="103" width="195" height="160" rx="60" fill="var(--sketch)" opacity="0.55" role="img" aria-label="Line illustration of a leaping fish"/>

  <text class="headline" x="172" y="100" font-size="72">Let's</text>
  <text class="headline" x="55" y="210" font-size="150">Grab a</text>
  <text class="headline" x="120" y="340" font-size="150">Bite to</text>
  <text class="headline" x="300" y="425" font-size="150">Eat</text>

  <text class="brand-name" x="1645" y="115" font-size="58" text-anchor="middle">THE DRIFTMILL</text>

  <text class="offers-title" x="1140" y="330" font-size="44">MARROWIND OFFERS</text>
  <text class="offers-list" y="388" font-size="38">
    <tspan x="1140">Lodging</tspan>
    <tspan x="1262">|</tspan>
    <tspan x="1293">Water Skiing</tspan>
    <tspan x="1480">|</tspan>
    <tspan x="1512">Camping</tspan>
  </text>
  <text class="offers-list" y="438" font-size="38">
    <tspan x="1140">Fishing</tspan>
    <tspan x="1252">|</tspan>
    <tspan x="1283">Hunting</tspan>
    <tspan x="1405">|</tspan>
    <tspan x="1435">Off Road Adventure</tspan>
  </text>
</svg>
</body>
</html>
```